Every sort of trade everysortoftrade.ca

Website for company offering Every sort of trade
Welding/Fabrication/Metal repairs/Metal building, Electrical repairs and installations, Plumbing and Heating, Renovations, Flooring, Paiting, and other services

We need a very clean and professional website outlining the many services we have

We would like each type of service to have its own page, with images of those types of services on those pages.

Then in the future, we can update those pages with projects we have done of those types.

Every Sort of Trade . CA

Located in Calgary, Alberta, Canada, offering services Alberta wide

Welding/Fabrication/Repair/Building - Steel and metals
Electrical contractor - Journeyman , small or large projects
Plumbing and Heating
Renovations
Flooring
Painting
Other services - storage, trucking, delivery, etc

business and residential services

Contractor

Coded - Design and coding required

5+ page

Sans Serif

3176b5
0253a1
85acd3
85abd2
cedeed
ffffff

Must have
• Clean
• Professional
• Easy of updating text and images

```html
<!DOCTYPE html>
<html lang="en">
<head>
<meta charset="utf-8">
<title>Every Sort of Trade</title>
<link rel="stylesheet" href="https://fonts.googleapis.com/css2?family=Oswald:wght@400;500;600&family=Raleway:wght@300;400&display=swap">
<style>
:root{
  --blue:#3176b5;
  --blue-deep:#0253a1;
  --blue-soft:#85acd3;
  --blue-pale:#cedeed;
  --ink:#111;
  --text:#8a8a8a;
  --white:#ffffff;
  --band:#f5f5f5;
  --line:#dcdcdc;
}
*{margin:0;padding:0;box-sizing:border-box}
html,body{width:1200px;height:3930px;overflow:hidden;background:var(--white)}
body{position:relative;font-family:'Raleway',sans-serif;color:var(--ink)}
.abs{position:absolute}
.heading{font-family:'Oswald',sans-serif;font-weight:500;text-transform:uppercase;letter-spacing:.2px}
.btn{position:absolute;display:flex;align-items:center;justify-content:center;background:var(--blue);color:var(--white);font-family:'Oswald',sans-serif;font-weight:500;font-size:14px;text-transform:uppercase;letter-spacing:.5px;width:160px;height:50px}
.body-copy{position:absolute;width:380px;font-size:14px;line-height:24px;color:var(--text);font-weight:300}
.photo{position:absolute;width:421px;height:283px}

/* hero */
.hero{left:0;top:0;width:1200px;height:576px;background:
  radial-gradient(ellipse 260px 160px at 1010px 420px,rgba(196,150,120,.85),rgba(196,150,120,0) 70%),
  radial-gradient(ellipse 200px 60px at 900px 170px,rgba(214,196,40,.55),rgba(214,196,40,0) 70%),
  radial-gradient(ellipse 90px 180px at 620px 320px,rgba(200,205,212,.8),rgba(200,205,212,0) 70%),
  radial-gradient(ellipse 60px 70px at 520px 520px,rgba(170,60,40,.7),rgba(170,60,40,0) 70%),
  linear-gradient(100deg,#2f3136 0%,#4b4d52 35%,#8c8e92 55%,#c9cbcd 75%,#b7b8b9 100%)}
.hero-shade{left:0;top:0;width:1200px;height:576px;background:linear-gradient(90deg,rgba(20,22,26,.55),rgba(20,22,26,.1))}
.brand{font-family:'Oswald',sans-serif;font-weight:500;font-size:28px;text-transform:uppercase;color:var(--white)}
.nav{top:46px;left:576px;font-family:'Oswald',sans-serif;font-size:11px;text-transform:uppercase;color:var(--white)}
.nav span{position:absolute;white-space:nowrap}
.nav .active{border-bottom:2px solid var(--blue);padding-bottom:6px}
.hero-phone{left:895px;top:41px;display:flex;align-items:center;gap:8px;font-family:'Oswald',sans-serif;font-size:17px;color:var(--white)}
.hero-title{left:184px;top:194px;font-size:32px;line-height:42px;color:var(--white)}
.hero-copy{left:184px;top:303px;width:360px;font-size:14px;line-height:24px;color:#ddd;font-weight:300}
.dots{left:190px;top:526px;display:flex;gap:12px}
.dots i{width:10px;height:10px;border-radius:50%;background:var(--white);display:block}
.dots i.on{background:var(--blue-soft)}

/* services */
.section-title{font-family:'Oswald',sans-serif;font-weight:500;font-size:50px;color:var(--blue);text-transform:uppercase}
.svc-title{position:absolute;font-size:28px;line-height:40px;color:var(--ink)}
.call-box{left:189px;top:1095px;width:819px;height:76px;border:1px solid var(--line);background:#fbfbfb;display:flex;align-items:center;justify-content:center;font-family:'Oswald',sans-serif;font-weight:500;font-size:32px;text-transform:uppercase;color:var(--blue-deep)}
.call-box em{font-style:normal;color:var(--blue);margin-left:10px}

.ph-plumbing{background:
  radial-gradient(ellipse 120px 140px at 110px 150px,rgba(48,72,160,.95),rgba(48,72,160,0) 75%),
  radial-gradient(ellipse 80px 90px at 170px 90px,rgba(222,186,160,.8),rgba(222,186,160,0) 70%),
  radial-gradient(ellipse 90px 70px at 300px 110px,rgba(190,60,50,.45),rgba(190,60,50,0) 70%),
  linear-gradient(90deg,#3a56a8 0%,#6f86c4 35%,#e6e9ee 60%,#f4f5f6 100%)}
.ph-welding{background:
  radial-gradient(circle at 220px 175px,#d9ecff 0%,#7fb2f0 6%,rgba(60,110,200,.55) 18%,rgba(20,30,60,0) 40%),
  radial-gradient(ellipse 140px 90px at 110px 150px,rgba(120,100,90,.55),rgba(120,100,90,0) 70%),
  linear-gradient(180deg,#0c0e16 0%,#141a2a 60%,#1d2538 100%)}
.ph-electrical{background:
  radial-gradient(ellipse 150px 160px at 290px 160px,rgba(40,56,140,.95),rgba(40,56,140,0) 75%),
  radial-gradient(ellipse 60px 50px at 190px 215px,rgba(230,200,60,.7),rgba(230,200,60,0) 70%),
  radial-gradient(ellipse 60px 60px at 250px 150px,rgba(222,186,160,.7),rgba(222,186,160,0) 70%),
  linear-gradient(90deg,#cfd1d4 0%,#e4e5e7 35%,#8c95b4 65%,#2e3e86 100%)}
.ph-renovation{background:
  linear-gradient(180deg,rgba(0,0,0,0) 0%,rgba(0,0,0,0) 63%,#9c6a3e 64%,#b88352 80%,#8a5a32 100%),
  radial-gradient(ellipse 40px 60px at 160px 90px,rgba(250,235,200,.9),rgba(250,235,200,0) 70%),
  radial-gradient(ellipse 40px 60px at 270px 90px,rgba(250,235,200,.9),rgba(250,235,200,0) 70%),
  linear-gradient(90deg,#e9e2d8 0%,#f2ede6 25%,#6b4a36 37%,#5a3d2c 63%,#f2ede6 75%,#e6ddd2 100%)}
.ph-flooring{background:
  radial-gradient(ellipse 120px 120px at 100px 180px,rgba(120,95,80,.85),rgba(120,95,80,0) 75%),
  linear-gradient(180deg,rgba(255,255,255,0) 60%,rgba(215,205,190,.6) 100%),
  linear-gradient(90deg,#8a7a6c 0%,#b3a18e 35%,#a39282 49%,#e8ebee 51%,#f6f7f8 75%,#dfe2e5 100%)}
.ph-painting{background:
  radial-gradient(ellipse 110px 140px at 70px 150px,rgba(90,90,95,.95),rgba(90,90,95,0) 75%),
  radial-gradient(ellipse 50px 50px at 80px 60px,rgba(200,160,130,.8),rgba(200,160,130,0) 70%),
  radial-gradient(ellipse 70px 50px at 230px 160px,rgba(200,60,50,.45),rgba(200,60,50,0) 70%),
  linear-gradient(90deg,#4c545e 0%,#98a9b4 30%,#cfe7ef 55%,#b8dde9 100%)}

/* locations */
.locations{left:0;top:3191px;width:1200px;height:650px;background:var(--band)}
.tabs{top:3332px;left:0;width:1200px;display:flex;justify-content:center;gap:40px;font-family:'Oswald',sans-serif;font-weight:500;font-size:20px;text-transform:uppercase}
.tabs span.on{border-bottom:3px solid var(--blue);padding-bottom:6px}
.map{left:189px;top:3406px;width:819px;height:335px;background:
  radial-gradient(ellipse 170px 150px at 540px 170px,rgba(236,190,180,.75),rgba(236,190,180,0) 80%),
  radial-gradient(ellipse 200px 120px at 180px 120px,rgba(184,210,170,.9),rgba(184,210,170,0) 80%),
  radial-gradient(ellipse 180px 110px at 700px 280px,rgba(210,222,200,.9),rgba(210,222,200,0) 80%),
  linear-gradient(135deg,#d4dec9 0%,#e8e7dd 45%,#e3e1d6 70%,#cfdac4 100%)}

/* footer */
.footer-brand{left:189px;top:3868px;font-size:26px;color:var(--ink)}
.copyright{left:752px;top:3885px;font-size:10px;text-transform:uppercase;color:var(--ink);letter-spacing:.4px}
</style>
</head>
<body>

<div class="abs hero" role="img" aria-label="Plumber tightening a pipe fitting under a sink with a wrench"></div>
<div class="abs hero-shade"></div>
<div class="abs brand" style="left:184px;top:34px">Every Sort of Trade</div>
<nav class="abs nav">
  <span class="active" style="left:0">Home</span>
  <span style="left:53px">About Us</span>
  <span style="left:124px">Services</span>
  <span style="left:192px">FAQ's</span>
  <span style="left:244px">Contact Us</span>
</nav>
<div class="abs hero-phone">
  <svg width="16" height="16" viewBox="0 0 24 24" fill="#ffffff"><path d="M6.6 10.8a15.1 15.1 0 0 0 6.6 6.6l2.2-2.2a1 1 0 0 1 1-.25 11.4 11.4 0 0 0 3.6.57 1 1 0 0 1 1 1V20a1 1 0 0 1-1 1A17 17 0 0 1 3 4a1 1 0 0 1 1-1h3.5a1 1 0 0 1 1 1c0 1.25.2 2.450.57 3.57a1 1 0 0 1-.25 1z"/></svg>
  555-010-4821
</div>
<h1 class="abs heading hero-title">24/7 Emergency<br>Service</h1>
<p class="abs hero-copy">Sed ut perspiciatis unde omnis iste natus error sit voluptatem accusantium doloremque</p>
<a class="btn" style="left:186px;top:383px;width:165px;height:65px">Learn More</a>
<div class="abs dots"><i class="on"></i><i></i><i></i><i></i></div>

<h2 class="abs section-title" style="left:184px;top:646px">Our Services</h2>

<h3 class="heading svc-title" style="left:197px;top:761px">Plumbing and Heating</h3>
<p class="body-copy" style="left:197px;top:835px">Sed ut perspiciatis unde omnis iste natus error sit voluptatem accusantium doloremque laudantium, totam rem aperiam, eaque ipsa quae ab illo inventore veritatis et quasi architecto beatae vitae dicta sunt explicabo.</p>
<a class="btn" style="left:197px;top:972px">Read More</a>
<div class="photo ph-plumbing" style="left:587px;top:768px" role="img" aria-label="Technician in a blue uniform working on a heating pipe"></div>

<div class="abs call-box">Call 555-010-7736 <em>for emergencies</em></div>

<div class="photo ph-welding" style="left:189px;top:1221px" role="img" aria-label="Welder working on metal with sparks flying"></div>
<h3 class="heading svc-title" style="left:631px;top:1215px">Welding/Fabrication/<br>Metal Repairs/ Metal Building</h3>
<p class="body-copy" style="left:633px;top:1315px">Sed ut perspiciatis unde omnis iste natus error sit voluptatem accusantium doloremque laudantium, totam rem aperiam, eaque ipsa quae ab illo inventore veritatis et quasi architecto beatae vitae dicta sunt explicabo.</p>
<a class="btn" style="left:637px;top:1454px">Read More</a>

<h3 class="heading svc-title" style="left:191px;top:1598px">Electrical Repairs &amp;<br>Installations</h3>
<p class="body-copy" style="left:191px;top:1697px">Sed ut perspiciatis unde omnis iste natus error sit voluptatem accusantium doloremque laudantium, totam rem aperiam, eaque ipsa quae ab illo inventore veritatis et quasi architecto beatae vitae dicta sunt explicabo.</p>
<a class="btn" style="left:192px;top:1826px">Read More</a>
<div class="photo ph-electrical" style="left:589px;top:1609px" role="img" aria-label="Electrician testing an electrical panel with a multimeter"></div>

<div class="photo ph-renovation" style="left:189px;top:2015px" role="img" aria-label="Renovated room with wooden floor and a feature wall"></div>
<h3 class="heading svc-title" style="left:637px;top:2013px">Renovations</h3>
<p class="body-copy" style="left:637px;top:2085px">Sed ut perspiciatis unde omnis iste natus error sit voluptatem accusantium doloremque laudantium, totam rem aperiam, eaque ipsa quae ab illo inventore veritatis et quasi architecto beatae vitae dicta sunt explicabo.</p>
<a class="btn" style="left:637px;top:2224px">Read More</a>

<h3 class="heading svc-title" style="left:197px;top:2443px">Flooring</h3>
<p class="body-copy" style="left:197px;top:2513px">Sed ut perspiciatis unde omnis iste natus error sit voluptatem accusantium doloremque laudantium, totam rem aperiam, eaque ipsa quae ab illo inventore veritatis et quasi architecto beatae vitae dicta sunt explicabo.</p>
<a class="btn" style="left:197px;top:2641px">Read More</a>
<div class="photo ph-flooring" style="left:587px;top:2426px" role="img" aria-label="Before and after view of a room under renovation and the finished kitchen"></div>

<div class="photo ph-painting" style="left:189px;top:2811px" role="img" aria-label="Painter rolling light blue paint onto a wall"></div>
<h3 class="heading svc-title" style="left:637px;top:2807px">Painting</h3>
<p class="body-copy" style="left:637px;top:2881px">Sed ut perspiciatis unde omnis iste natus error sit voluptatem accusantium doloremque laudantium, totam rem aperiam, eaque ipsa quae ab illo inventore veritatis et quasi architecto beatae vitae dicta sunt explicabo.</p>
<a class="btn" style="left:637px;top:3023px">Read More</a>

<section class="abs locations"></section>
<h2 class="abs section-title" style="left:0;top:3232px;width:1200px;text-align:center">Locations</h2>
<div class="abs tabs"><span class="on">Calgary</span><span>Alberta</span><span>Canada</span></div>
<div class="abs map" role="img" aria-label="Road map of Calgary and surrounding area with service region highlighted"></div>

<div class="abs heading footer-brand">Every Sort of Trade</div>
<div class="abs copyright">© 2017 Company Name | All Rights Reserved</div>

</body>
</html>
```